Offshore Energy Projects Management Consultancy needs a business card design

Logo available. We provide teams to deliver engineering consultancy, project management and delivery teams mainly in the offshore renewables sector. The company is all about bringing the right people to a project to deliver the scope.

The business card will be used for all staff.

The business card should be quite simple, vibrant and uncluttered but convey experience, enthusiasm and integration.

Target Market(s)

Energy Project Developers and Tier 1 construction companies

Contact Information for Business Card

Logo should be on the back of the card. I'm happy for the designer to play with the colour of the logo and background colour.

Front of the card should convey all the must have information in a clear and professional manner but without being overly traditional.

Colors

Designer to choose colors to be used in the design.

Requirements
Must have
• Land Line Tel Number, Mobile Tel Number, Email, business address, web address.

```html
<!DOCTYPE html>
<html lang="en">
<head>
<meta charset="utf-8">
<title>Tidewater Delivery Group – Business Card</title>
<link rel="stylesheet" href="https://fonts.googleapis.com/css2?family=Open+Sans:wght@400;600;700&display=swap">
<style>
  :root {
    --brand-blue: #1176c2;
    --brand-blue-deep: #0f6cb6;
    --accent-blue: #2aa7e2;
    --title-blue: #5cc4f2;
    --card-white: #ffffff;
    --stage: #e4e6e8;
    --text-light: #ffffff;
  }
  * { box-sizing: border-box; margin: 0; padding: 0; }
  html, body { width: 1200px; height: 800px; overflow: hidden; }
  body {
    background: var(--stage);
    font-family: "Open Sans", sans-serif;
    position: relative;
  }
  .card {
    position: absolute;
    width: 560px;
    height: 320px;
    box-shadow: 0 6px 18px rgba(0,0,0,0.18);
    overflow: hidden;
  }
  .card-back { left: 320px; top: 50px; background: var(--brand-blue); }
  .card-front { left: 320px; top: 420px; background: var(--card-white); }

  .brand-name {
    font-weight: 700;
    letter-spacing: 1px;
    text-align: center;
    line-height: 1.15;
  }
  .card-back .brand-name {
    position: absolute; left: 0; right: 0; top: 100px;
    color: var(--text-light);
    font-size: 26px;
  }
  .brand-name .tagline-line { display: block; font-size: 15px; letter-spacing: 7px; }

  .back-footer {
    position: absolute; left: 40px; right: 40px; top: 240px;
    display: flex; align-items: center; gap: 16px;
    color: var(--text-light);
    font-size: 14px; letter-spacing: 2.5px;
  }
  .back-footer .rule { flex: 1; height: 1px; background: rgba(255,255,255,0.35); }

  .front-shape { position: absolute; inset: 0; }
  .card-front .brand-name {
    position: absolute; left: 20px; top: 118px; width: 250px;
    color: var(--brand-blue-deep);
    font-size: 21px;
  }
  .card-front .brand-name .tagline-line { font-size: 12px; letter-spacing: 6px; }

  .contact {
    position: absolute; left: 330px; top: 44px; width: 220px;
    color: var(--text-light);
  }
  .contact-name { font-size: 19px; font-weight: 700; }
  .contact-role { font-size: 13px; color: var(--title-blue); margin-top: -2px; }
  .contact-rule { width: 36px; height: 1px; background: rgba(255,255,255,0.8); margin: 12px 0 16px; }
  .contact-address { font-size: 13.5px; line-height: 1.35; margin-bottom: 10px; }
  .contact-list { list-style: none; font-size: 13.5px; line-height: 1.45; }
  .contact-list li { display: flex; align-items: center; gap: 7px; }
  .contact-list svg { width: 13px; height: 13px; flex: none; }
</style>
</head>
<body>
  <section class="card card-back" aria-label="Card back">
    <div class="brand-name">TIDEWATER DELIVERY<span class="tagline-line">GROUP</span></div>
    <div class="back-footer">
      <span class="rule"></span>
      <span class="web">www.tdg.ltd</span>
      <span class="rule"></span>
    </div>
  </section>

  <section class="card card-front" aria-label="Card front">
    <svg class="front-shape" viewBox="0 0 560 320" width="560" height="320" aria-hidden="true">
      <path d="M282 0 C300 130 250 255 140 320 L150 320 C262 258 312 130 300 0 Z" fill="var(--accent-blue)"/>
      <path d="M302 0 C318 135 270 262 165 320 L560 320 L560 0 Z" fill="var(--brand-blue)"/>
    </svg>

    <div class="brand-name">TIDEWATER DELIVERY<span class="tagline-line">GROUP</span></div>

    <div class="contact">
      <p class="contact-name">Martin Halvorsen</p>
      <p class="contact-role">Director</p>
      <div class="contact-rule"></div>
      <p class="contact-address">Northgate House<br>118 Marine Street<br>Portlen, PL4 2XR</p>
      <ul class="contact-list">
        <li><svg viewBox="0 0 14 14"><rect x="3.5" y="1" width="7" height="12" rx="1.3" fill="none" stroke="#fff" stroke-width="1.2"/><circle cx="7" cy="11" r="0.7" fill="#fff"/></svg>+44 1632 960 418</li>
        <li><svg viewBox="0 0 14 14"><path d="M3 1.5 L5.2 1.5 L6 4.5 L4.6 5.6 C5.3 7.3 6.7 8.7 8.4 9.4 L9.5 8 L12.5 8.8 L12.5 11 C12.5 12 11.7 12.6 10.8 12.5 C6 12 2 8 1.5 3.2 C1.4 2.3 2 1.5 3 1.5 Z" fill="#fff"/></svg>+44 1632 960 512</li>
        <li><svg viewBox="0 0 14 14"><rect x="1" y="3" width="12" height="8.5" fill="none" stroke="#fff" stroke-width="1.2"/><path d="M1 3.3 L7 8 L13 3.3" fill="none" stroke="#fff" stroke-width="1.2"/></svg>martin@tdg.ltd</li>
        <li><svg viewBox="0 0 14 14"><circle cx="7" cy="7" r="5.6" fill="none" stroke="#fff" stroke-width="1.1"/><ellipse cx="7" cy="7" rx="2.4" ry="5.6" fill="none" stroke="#fff" stroke-width="1"/><path d="M1.4 7 H12.6" stroke="#fff" stroke-width="1"/></svg>www.tdg.ltd</li>
      </ul>
    </div>
  </section>
</body>
</html>
```